Box Design for Organic Bamboo Hooded Baby Bath Towels

Box size 25 x 18 x 6cm, attached PDF from supplier for reference, and our logo

We need a box designed for a new company based in Orange County, called Lumo Little Ones. Our company specializes in quality, upscale, health conscious products for infants, babies and toddlers. Our first product launching is a hooded bath towel made of organic bamboo. We would like to see a design that signifies purity, simplicity, safety, and elegance. The colors we like are white, blue (like the shade in our logo attached), greens, and grays.

Front of box:
Needs to include logo

Key Points:
*Unbleached, chemical & toxin free
*Hypoallergenic and Antibacterial
*Three times more absorbent than cotton
*Eco Friendly

Somewhere on the front it needs to note sizing: 30x30 inches
Includes bonus wash cloth

Back of Box:

Do you ever find yourself questioning what products are best for your little one? We thought so. So do we! We are mamas here at Lumo Little Ones, and nothing is more important to us than the well-being of our little ones. 100% organic bamboo is the best of the best for our bundles of joy, being ultra soft, antibacterial, hypoallergenic, free of dyes & chemicals, and 3x more absorbent than cotton. These towels will leave your baby cozy, dry, and happily wrapped up in a silky soft embrace after bath time. From our mama hearts, to yours.

Care Instructions:
-Machine Wash
-Hand Wash
-Do not Dry Clean
-Do not Bleach
-Do not Tumble Dry

Additional Care Tips:
-Wash before first use
-Do not store wet bath towel
-Store in a well aired room (never in a sealed container, plastic bag, etc)
-Avoid contact with rough surfaces which could loosen the yarns
-Do not bleach or use fabric softeners. Dryer sheets are also not recommended
-Keep away from open flames or electric heaters
-If towel is used after swimming pools, sea water, chlorinated water, please be sure to wash immediately after to prevent the bamboo fibre from weakening

Designed in the US, Made in China
Lumo Little Ones
info@lumolittleones.com

Target Market(s)

Moms

Industry/Entity Type

Baby

Font styles to use
Serif
Script

Colors
85cae6
eea4c8
ecf7fb
ffffff
d9d9d9
fdf9cf
cadf82
eaf2ce

Requirements
Must have
• the key info written in project description, our logo, company name, where it's made
Nice to have
• designs that communicate organic, purity & safety
• the yellow & green do not need to be used. If you have an idea and would like to include those colors, we have selected a yellow and two greens that would work with our vision. If you feel otherwise, please let us know why :)
Should not have
• it cannot look busy

```html
<!DOCTYPE html>
<html lang="en">
<head>
<meta charset="utf-8">
<title>Lumo Little Ones – Hooded Baby Towel Box</title>
<link rel="stylesheet" href="https://fonts.googleapis.com/css2?family=Space+Mono:wght@700&family=Rubik:wght@800&family=Cormorant+Garamond:wght@600&display=swap">
<style>
  :root {
    --stage: #eef1f4;
    --white: #ffffff;
    --sky: #85cae6;
    --sky-light: #a8dcf1;
    --sky-side: #8cc9e4;
    --sky-pale: #ecf7fb;
    --grey-line: #d9d9d9;
    --pink: #eea4c8;
    --navy: #2a4a96;
    --badge-blue: #3d62b0;
    --badge-blue-dark: #2d4f9e;
    --logo-blue: #1d9cc4;
  }
  * { margin: 0; padding: 0; box-sizing: border-box; }
  html, body { width: 1200px; height: 864px; overflow: hidden; background: var(--stage); }
  .stage { position: relative; width: 1200px; height: 864px; }

  .panel { position: absolute; overflow: hidden; box-shadow: 0 6px 20px rgba(40, 70, 110, 0.12); }

  /* Top panel 25 x 6 cm */
  .box-top {
    left: 135px; top: 72px; width: 750px; height: 180px;
    background: var(--white);
    border-bottom: 1px solid var(--grey-line);
  }
  .box-top .rule { position: absolute; left: 0; right: 0; height: 2px; background: var(--sky-pale); }
  .box-top .rule.is-upper { top: 24px; }
  .box-top .rule.is-lower { bottom: 24px; }
  .top-brand {
    position: absolute; left: 0; right: 0; top: 60px; text-align: center;
    font-family: "Cormorant Garamond", serif; font-weight: 600;
    font-size: 50px; line-height: 1; color: var(--logo-blue);
  }

  /* Front panel 25 x 18 cm */
  .box-front { left: 135px; top: 252px; width: 750px; height: 540px; background: var(--white); }
  .wave-band { position: absolute; inset: 0; width: 100%; height: 100%; }

  .brand-name {
    position: absolute; left: 40px; top: 34px;
    font-family: "Cormorant Garamond", serif; font-weight: 600;
    font-size: 66px; line-height: 1; color: var(--logo-blue);
  }

  .feature-list { position: absolute; left: 26px; top: 140px; list-style: none; }
  .feature { display: flex; align-items: center; gap: 10px; margin-bottom: 6px; }
  .feature-icon { width: 22px; height: 22px; flex: none; }
  .feature-label {
    font-family: "Space Mono", monospace; font-weight: 700;
    color: var(--white); border-radius: 4px 12px 12px 4px;
    padding: 5px 12px; line-height: 1.1;
  }
  .feature-label.is-primary { background: linear-gradient(90deg, var(--badge-blue-dark), var(--badge-blue)); font-size: 17px; width: 260px; }
  .feature-label.is-accent { background: linear-gradient(90deg, var(--pink), #c9a6d8); font-size: 12px; width: 260px; }
  .feature-label.is-secondary { background: linear-gradient(90deg, var(--badge-blue-dark), var(--badge-blue)); font-size: 12px; width: 260px; }

  .mascot-art {
    position: absolute; left: 85px; top: 318px; width: 80px; height: 80px;
    border-radius: 50%;
    background: radial-gradient(circle at 50% 45%, #6f8fb1, #5478a0 60%, rgba(84,120,160,0) 72%);
  }
  .bonus-note {
    position: absolute; left: 14px; top: 408px; width: 230px;
    font-family: "Space Mono", monospace; font-weight: 700; font-size: 19px;
    color: var(--navy); text-align: center; line-height: 1;
  }

  .baby-photo {
    position: absolute; left: 380px; top: 160px; width: 370px; height: 380px;
    background: radial-gradient(ellipse at 50% 42%, #f7f7f7 0%, #ebe7e6 35%, #e7cfc4 50%, rgba(168,220,241,0.4) 76%, rgba(168,220,241,0) 100%);
  }

  .claim {
    position: absolute; left: 240px; top: 440px; width: 200px;
    font-family: "Space Mono", monospace; font-weight: 700; font-size: 17px;
    color: var(--pink); text-align: center; line-height: 1;
  }

  .product-title {
    position: absolute; left: 530px; top: 348px; width: 210px;
    font-family: "Rubik", sans-serif; font-weight: 800; font-size: 42px; line-height: 1;
  }
  .product-title .line { display: block; }
  .product-title .is-white { color: var(--white); }
  .product-title .is-pink { color: var(--pink); }
  .product-size { display: block; margin-top: 8px; color: var(--navy); font-size: 40px; }

  /* Side panel 6 x 18 cm */
  .box-side { left: 885px; top: 252px; width: 180px; height: 540px; background: var(--sky-side); }
  .side-copy {
    position: absolute; left: 0; top: 0; width: 180px; height: 540px;
    display: flex; justify-content: center; align-items: center; gap: 18px;
    writing-mode: vertical-rl; transform: rotate(180deg);
  }
  .side-note {
    font-family: "Space Mono", monospace; font-weight: 700; font-size: 26px;
    color: var(--navy); line-height: 1; text-align: center;
  }
  .side-brand {
    font-family: "Cormorant Garamond", serif; font-weight: 600;
    font-size: 30px; line-height: 1; color: var(--logo-blue);
  }
</style>
</head>
<body>
<main class="stage">
  <section class="panel box-top" aria-label="Top panel">
    <span class="rule is-upper"></span>
    <p class="top-brand">Lumo Little Ones</p>
    <span class="rule is-lower"></span>
  </section>

  <section class="panel box-front" aria-label="Front panel">
    <svg class="wave-band" viewBox="0 0 750 540" preserveAspectRatio="none" aria-hidden="true">
      <path d="M0 235 C 120 290, 270 320, 430 295 C 570 272, 670 210, 750 190 L750 540 L0 540 Z" fill="var(--sky-light)"/>
      <path d="M0 252 C 130 312, 280 338, 440 310 C 580 286, 680 228, 750 210" fill="none" stroke="var(--white)" stroke-width="12"/>
      <path d="M0 533 L750 533 L750 540 L0 540 Z" fill="var(--sky)"/>
    </svg>

    <h1 class="brand-name">Lumo Little Ones</h1>

    <ul class="feature-list">
      <li class="feature">
        <svg class="feature-icon" viewBox="0 0 26 26" aria-hidden="true"><path d="M5 21 C5 10 12 5 22 4 C21 14 16 21 5 21 Z M5 21 L15 11" fill="none" stroke="var(--badge-blue)" stroke-width="2.2"/></svg>
        <span class="feature-label is-primary">Eco Friendly</span>
      </li>
      <li class="feature">
        <svg class="feature-icon" viewBox="0 0 26 26" aria-hidden="true"><rect x="3" y="10" width="20" height="12" rx="2" fill="none" stroke="var(--badge-blue)" stroke-width="2"/><path d="M13 3 C11 6 11 8 13 8 C15 8 15 6 13 3 Z" fill="var(--badge-blue)"/></svg>
        <span class="feature-label is-accent">Three times more<br>absorbent than cotton</span>
      </li>
      <li class="feature">
        <svg class="feature-icon" viewBox="0 0 26 26" aria-hidden="true"><path d="M5 6 L21 22 M21 6 L5 22" stroke="var(--badge-blue)" stroke-width="3"/></svg>
        <span class="feature-label is-secondary">Unbleached, chemical<br>&amp; toxin free</span>
      </li>
    </ul>

    <div class="mascot-art" role="img" aria-label="Illustration of a small panda holding bamboo leaves"></div>
    <p class="bonus-note">INCLUDES BONUS<br>WASH CLOTH</p>

    <div class="baby-photo" role="img" aria-label="Photo of a baby wrapped in a white hooded towel"></div>

    <p class="claim">Hypoallergenic<br>and<br>Antibacterial</p>

    <h2 class="product-title">
      <span class="line is-white">HOODED</span>
      <span class="line is-pink">BABY</span>
      <span class="line is-white">TOWEL</span>
      <span class="product-size">30x30"</span>
    </h2>
  </section>

  <section class="panel box-side" aria-label="Side panel">
    <div class="side-copy">
      <p class="side-note">INCLUDES BONUS<br>WASH CLOTH</p>
      <p class="side-brand">Lumo Little Ones</p>
    </div>
  </section>
</main>
</body>
</html>
```